Awesome Office Furniture Dealer's Brochure!

Need a professional and informative brochure put together for our clients - may need separate designs for Government and Education clients. Should be based of our new website design and feel. Sections should include: Manufacturers we carry, services, and statements about our company - who we are & what we do. Brochure is 8.5 x 11 in tri-fold configuration. Template files attached.

Target Market(s)

Small to Medium businesses

Industry/Entity Type

Office Furniture

Requirements
Must have
• Look and feel of our website www.pembrills.com. Images can be taken from any of our vendors listed under /products, look to VEX primarily. We will get the final designer production ready images when needed.
Nice to have
• Incorporate the "love your workspace" from our website.

```html
<!DOCTYPE html>
<html lang="en">
<head>
<meta charset="utf-8">
<title>Pembrill's Office Furniture – Tri-fold Brochure</title>
<link rel="stylesheet" href="https://fonts.googleapis.com/css2?family=Didact+Gothic&family=Raleway:wght@600;700;800&family=Kaushan+Script&display=swap">
<style>
:root{
  --green:#7dc242;
  --ink:#3a3a3a;
  --grey:#8a8a8a;
  --grey-dark:#4f5254;
  --paper:#ffffff;
  --backdrop:#ececec;
  --body:"Didact Gothic", sans-serif;
  --head:"Raleway", sans-serif;
  --script:"Kaushan Script", cursive;
}
*{box-sizing:border-box;margin:0;padding:0}
html,body{width:1200px;height:441px;overflow:hidden;background:var(--backdrop)}
body{position:relative;font-family:var(--body);color:var(--ink)}
.spread{position:absolute;top:15px;width:531px;height:410px;display:flex;background:var(--paper);box-shadow:0 2px 6px rgba(0,0,0,.18)}
.spread--outside{left:46px}
.spread--inside{left:623px}
.panel{position:relative;width:177px;height:100%;overflow:hidden;border-right:1px solid #e3e3e3}
.panel:last-child{border-right:0}
.photo{background:linear-gradient(135deg,#d9dcdd,#9fa4a6)}
.copy{font-size:5.6px;line-height:1.45;color:var(--ink)}
.copy p{margin-bottom:4px}
.hl{color:var(--green);font-weight:700}

/* plain company name */
.brand-name{font-family:var(--body);font-weight:400;color:var(--green);text-align:center;line-height:1.15}

/* intro panel */
.intro .copy{padding:14px 12px 8px}
.feature-row{display:flex;height:88px;margin-bottom:4px}
.feature-row .photo{flex:1}
.feature-row .tab{width:30px;background:var(--green);display:flex;align-items:center;justify-content:center}
.tab span{writing-mode:vertical-rl;font-family:var(--head);font-weight:800;font-size:11px;color:#fff;letter-spacing:.5px}
.photo--products{background:linear-gradient(135deg,#f4f4f4,#d8c6ae 60%,#8e8e8e)}
.photo--solutions{background:linear-gradient(135deg,#e9e5de,#b9a48c)}
.photo--services{background:linear-gradient(180deg,#cfe3f1,#7fb75a 55%,#9a9a9a)}

/* back cover */
.back{display:flex;flex-direction:column;align-items:center;text-align:center}
.label{font-family:var(--head);font-weight:800;font-size:6.5px;color:var(--green);text-decoration:underline;margin-top:16px}
.maker{font-family:var(--body);font-size:22px;color:var(--grey);letter-spacing:2px;margin:8px 0}
.back .copy{padding:0 16px}
.badges{display:grid;grid-template-columns:repeat(3,1fr);gap:6px 8px;padding:8px 14px;width:100%}
.badge{height:14px;background:#dcdcdc;border-radius:2px}
.badge--round{border-radius:50%;height:22px;width:22px;justify-self:center}
.divider{width:100%;height:1px;background:#dcdcdc;margin:6px 0}
.showroom{font-size:5.6px;line-height:1.55;margin:6px 0}
.showroom h3{font-family:var(--body);font-weight:400;font-size:7px;color:var(--green);margin-bottom:1px}
.showroom .link{color:var(--green)}
.note{font-style:italic;font-size:5.4px;padding:0 18px;line-height:1.45}
.web-bar{margin-top:auto;width:100%;background:var(--green);color:#fff;font-family:var(--head);font-weight:700;font-size:6.5px;padding:4px 0}

/* front cover */
.cover .brand-name{position:absolute;top:66px;left:12px;right:12px;font-size:17px}
.cover-band{position:absolute;inset:0;background:var(--green);clip-path:polygon(0 45%,100% 32%,100% 38.5%,0 51.5%)}
.cover-band-text{position:absolute;top:192px;left:8px;transform:rotate(-16.7deg);transform-origin:left center;font-family:var(--head);font-weight:800;font-size:7.6px;line-height:9px;color:#fff;white-space:nowrap}
.cover-photo{position:absolute;inset:0;clip-path:polygon(0 52.5%,100% 39.5%,100% 82%,0 100%);background:linear-gradient(160deg,#eef0f0,#bfc3c4 45%,#55585a)}
.tagline{position:absolute;top:262px;left:10px;transform:rotate(-17deg);transform-origin:left;font-family:var(--script);font-size:17px;color:#fff;white-space:nowrap;text-shadow:0 1px 2px rgba(0,0,0,.35)}
.corner{position:absolute;inset:0;background:var(--grey-dark);clip-path:polygon(100% 83%,100% 100%,48% 100%)}
.corner-text{position:absolute;right:6px;bottom:10px;transform:rotate(-17deg);transform-origin:right;text-align:right;font-family:var(--head);font-weight:800;font-size:7px;color:#fff;line-height:1.3}
.corner-text .accent{color:var(--green)}

/* inside */
.why{padding:14px 11px}
.heading{font-family:var(--head);font-weight:800;color:var(--green);line-height:1.05}
.why .heading{font-size:12.5px;margin-bottom:6px}
.why .copy{font-size:5.3px}
.photo--chair{height:84px;margin-top:4px;background:linear-gradient(180deg,#f5f5f5,#4a4a4a 55%,#f5f5f5)}
.about{display:flex;flex-direction:column}
.about .brand-name{font-size:13px;padding:16px 12px 8px}
.about .intro-line{font-size:5.8px;font-weight:700;padding:0 12px 6px}
.photo--office{height:82px;background:linear-gradient(180deg,#e8e4de,#c9c2b6 55%,#8a6a4e)}
.about .heading{font-size:13px;padding:10px 12px 5px}
.value{padding:0 12px;margin-bottom:5px;font-size:5.4px;line-height:1.45}
.value b{font-family:var(--head);color:var(--green);font-size:6.2px}
.services{padding:12px 10px}
.services .top{display:flex;gap:4px;align-items:flex-start}
.services .top .heading{font-size:13px}
.services .top .copy{font-size:5.2px;font-style:italic}
.grid{display:grid;grid-template-columns:1fr 1fr;gap:3px;margin:6px 0}
.cell{height:44px}
.cell-label{font-family:var(--head);font-weight:800;font-size:4.8px;color:var(--green);text-align:center;margin-top:1px}
.cell--plan{background:linear-gradient(135deg,#f3f3f3,#c7b49a)}
.cell--design{background:linear-gradient(135deg,#f0d26c,#d15b5b 50%,#5b83c6)}
.cell--render{background:linear-gradient(135deg,#f4f4f4,#a9a9a9)}
.cell--delivery{background:linear-gradient(135deg,#e6e6e6,#8b6a4f)}
.services .rental{font-size:12.5px;margin:8px 0 5px}
.photo--rental{height:58px;margin-top:6px;background:linear-gradient(135deg,#f2f2f2,#9c7b5c 60%,#555)}
</style>
</head>
<body>

<section class="spread spread--outside" aria-label="Brochure outside">
  <article class="panel intro">
    <div class="copy">
      <p>Since 1985, Pembrill's has been helping businesses large and small create workspaces that make sense. We try hard to make the process easy and, dare we say, fun. We are proud to feature product from <span class="hl">VEX</span> along with dozens of other makers, as well as being the region's best source for <span class="hl">used office furniture</span>. Please browse our site and see the latest in office furniture including desks, workstations, cubicles, common area, office chairs, and more. Then visit one of our showrooms in Harborview or Lakeside, or call to set up a consultation with one of our awesome associates.</p>
    </div>
    <div class="feature-row"><div class="photo photo--products" role="img" aria-label="Office chairs, desks and cabinets"></div><div class="tab"><span>PRODUCTS</span></div></div>
    <div class="feature-row"><div class="photo photo--solutions" role="img" aria-label="Overhead view of an open office layout"></div><div class="tab"><span>SOLUTIONS</span></div></div>
    <div class="feature-row"><div class="photo photo--services" role="img" aria-label="Delivery truck on the road"></div><div class="tab"><span>SERVICES</span></div></div>
  </article>

  <article class="panel back">
    <div class="label">OUR PRIMARY MANUFACTURER</div>
    <div class="maker">VEX</div>
    <div class="copy">VEX is a leading designer of workplace furniture and Pembrill's is proud to be a Diamond Level VEX dealer.</div>
    <div class="label">OUR FEATURED MANUFACTURERS</div>
    <div class="badges" aria-label="Partner manufacturers">
      <div class="badge"></div><div class="badge"></div><div class="badge badge--round"></div>
      <div class="badge"></div><div class="badge"></div><div class="badge"></div>
    </div>
    <div class="divider"></div>
    <div class="showroom">
      <h3>HARBORVIEW SHOWROOM</h3>
      18 Wharf Lane, Harborview 40120<br>
      hello@pembrills.com<br>
      <span class="link">555.010.2417</span><br>
      Monday – Friday 8:30am – 5pm<br>
      Saturday 10am – 4pm
    </div>
    <p class="note">Please call ahead on Saturdays for our Harborview location! We close for all major (and sometimes minor) holiday weekends.</p>
    <div class="showroom">
      <h3>LAKESIDE SHOWROOM</h3>
      2260 Cedar Row, Lakeside 40315<br>
      hello@pembrills.com<br>
      <span class="link">555.010.3388</span><br>
      Monday – Friday 8:30am – 5pm
    </div>
    <div class="web-bar">www.pembrills.com</div>
  </article>

  <article class="panel cover">
    <p class="brand-name">Pembrill's Office Furniture</p>
    <div class="cover-band"></div>
    <div class="cover-band-text">PRODUCTS, SOLUTIONS &amp; SERVICES</div>
    <div class="cover-photo" role="img" aria-label="Bright modern office with desks and task chairs"></div>
    <div class="tagline">Love Your Workspace</div>
    <div class="corner"></div>
    <div class="corner-text">Yep!<br><span class="accent">We do it all!</span></div>
  </article>
</section>

<section class="spread spread--inside" aria-label="Brochure inside">
  <article class="panel why">
    <h2 class="heading">WHY PEMBRILL'S OFFICE FURNITURE?</h2>
    <div class="copy">
      <p>Because we make buying office furniture easy.</p>
      <p>First, <span class="hl">we know what we are doing.</span> With over 30 years of experience in commercial furniture, you can count on our team to help you through the entire buying process, from design to product choice to final installation.</p>
      <p>Second, <span class="hl">we listen to our clients.</span> If you have a budget, we stick to it. If you don't like a product, we won't push it. We would rather lose a sale than sell something that won't work.</p>
      <p>Third, <span class="hl">we only sell what we believe in.</span> We choose makers that represent the best value in office furniture and we stand behind every item.</p>
      <p>Last, <span class="hl">we offer the best value proposition in our industry.</span> We provide free design and space planning, plus easy delivery and installation by our own crew.</p>
    </div>
    <div class="photo photo--chair" role="img" aria-label="Black mesh task chair"></div>
  </article>

  <article class="panel about">
    <p class="brand-name">Pembrill's Office Furniture</p>
    <p class="intro-line">Pembrill's Office Furniture has been providing the Northern Coast businesses with new and used furniture solutions for over 30 years.</p>
    <div class="photo photo--office" role="img" aria-label="Private office with wood desk and glass partition"></div>
    <h2 class="heading">OUR CORE VALUES</h2>
    <p class="value"><b>Dedication to Customer Service Excellence</b> We will meet and exceed customer needs and expectations with professional guidance and support.</p>
    <p class="value"><b>Honesty &amp; Integrity</b> We will conduct all of our activities with uncompromising honesty, integrity and the highest ethical standard.</p>
    <p class="value"><b>People Growth &amp; Development</b> We will show care and respect for all members of the Pembrill's team, their families, our neighbors, customers and suppliers.</p>
    <p class="value"><b>Product Quality</b> We will provide solutions that exemplify our commitment to value: products that are high quality, reasonably priced, and well designed.</p>
  </article>

  <article class="panel services">
    <div class="top">
      <h2 class="heading">SERVICES</h2>
      <p class="copy">From initial space planning to final installation, Pembrill's can help with every phase of your project.</p>
    </div>
    <div class="grid">
      <div><div class="cell cell--plan" role="img" aria-label="Floor plan drawing for space planning"></div><div class="cell-label">SPACE PLANNING</div></div>
      <div><div class="cell cell--design" role="img" aria-label="Fabric and finish swatches for design"></div><div class="cell-label">DESIGN</div></div>
      <div><div class="cell cell--render" role="img" aria-label="3D rendering of an office layout"></div><div class="cell-label">RENDER</div></div>
      <div><div class="cell cell--delivery" role="img" aria-label="Installed furniture after delivery"></div><div class="cell-label">DELIVERY &amp; INSTALLATION</div></div>
    </div>
    <h2 class="heading rental">OFFICE FURNITURE RENTAL</h2>
    <p class="copy">Pembrill's has a great selection of office furniture for short term and long term rental. Whether you need a large conference table or training setup for a short term rental, or workstations to house some extra employees for a year, Pembrill's has your office furniture rentals covered. Please contact us here or give us a call at 555.010.2417 to learn more.</p>
    <div class="photo photo--rental" role="img" aria-label="Rental desks and chairs arranged in a showroom"></div>
  </article>
</section>

</body>
</html>
```